Professional/modern business card design for construction company

We need a new business card design, double sided keeping it modern, sleek, professional and simple. We are an earthmoving business but do not want any pictures of machinery. I would like one side to have the logo and the other to have all the information, keeping with the colors in our logo. The business card will need to be able to be customised so we can use it for several different managers., we would also like to be able to use the design to apply it to other stationary ie. letterheads, notebooks etc. We do not really have a tag line but we could put on there that we specialise in - Agriculture, Civil Construction and Mining.

Contact Information for Business Card

Brolga Ridge Excavations Pty Ltd
ABN 58 402 937 615
82 Gumleaf Creek Road, Moree NSW 2400

Harold Benton
Managing Director
P 0418 639 204
E haroldbenton@brolgaridgeexc.com.au

Font styles to use
Serif
Sans Serif

Requirements
Nice to have
• I have attached some examples of ideas.
Should not have
• images of machinery

```html
<!DOCTYPE html>
<html lang="en">
<head>
<meta charset="utf-8">
<title>Brolga Ridge Excavations – Business Card</title>
<link href="https://fonts.googleapis.com/css2?family=Lato:wght@400;700;900&display=swap" rel="stylesheet">
<style>
  :root {
    --backdrop: #d9d9d9;
    --card-light: #fcf8f7;
    --charcoal: #3b3b3b;
    --charcoal-deep: #333333;
    --ink: #2f2f2f;
    --orange: #f5891f;
    --white: #ffffff;
    --rule: #e2dcda;
  }
  * { box-sizing: border-box; margin: 0; padding: 0; }
  html, body { width: 1200px; height: 782px; overflow: hidden; }
  body {
    background: var(--backdrop);
    font-family: "Lato", Arial, sans-serif;
    display: flex;
    align-items: center;
    justify-content: center;
    gap: 40px;
  }
  .card {
    position: relative;
    width: 540px;
    height: 330px;
    overflow: hidden;
    box-shadow: 0 6px 18px rgba(0,0,0,0.25);
  }

  /* Front */
  .card--front { background: var(--card-light); color: var(--ink); }
  .brand {
    position: absolute;
    left: 30px;
    top: 58px;
    width: 210px;
    display: flex;
    align-items: flex-start;
    gap: 10px;
  }
  .brand__mark {
    width: 14px; height: 14px;
    background: var(--orange);
    flex: none;
    margin-top: 6px;
  }
  .brand__name {
    font-weight: 900;
    font-size: 24px;
    line-height: 1.05;
    text-transform: uppercase;
    color: var(--charcoal);
    letter-spacing: 0.5px;
  }
  .divider {
    position: absolute;
    left: 272px;
    top: 54px;
    width: 1px;
    height: 170px;
    background: var(--rule);
  }
  .details {
    position: absolute;
    left: 290px;
    top: 54px;
    font-size: 13px;
    line-height: 1.25;
  }
  .details__name {
    font-weight: 900;
    font-size: 18px;
    color: var(--orange);
    text-transform: uppercase;
    letter-spacing: 0.4px;
  }
  .details__role { font-size: 12.5px; margin-bottom: 6px; }
  .details__company { color: var(--orange); font-weight: 700; }
  .details__address { margin-bottom: 8px; }
  .contact { list-style: none; }
  .contact li { display: flex; align-items: center; gap: 7px; font-size: 12.5px; line-height: 1.35; }
  .contact svg { width: 11px; height: 11px; flex: none; }
  .abn-band {
    position: absolute;
    left: 0; top: 0;
  }
  .abn {
    position: absolute;
    left: 30px;
    top: 240px;
    font-size: 14px;
    color: var(--white);
    letter-spacing: 0.3px;
  }
  .abn__label { color: var(--orange); }

  /* Back */
  .card--back {
    background: radial-gradient(ellipse at 60% 45%, #444444 0%, var(--charcoal-deep) 75%);
    color: var(--white);
  }
  .back__brand {
    position: absolute;
    left: 0; right: 0;
    top: 112px;
    display: flex;
    justify-content: center;
    align-items: center;
    gap: 10px;
  }
  .back__mark { width: 14px; height: 14px; background: var(--orange); }
  .back__name {
    font-weight: 900;
    font-size: 22px;
    text-transform: uppercase;
    letter-spacing: 0.5px;
  }
  .tagline {
    position: absolute;
    left: 0; right: 0;
    top: 168px;
    text-align: center;
  }
  .tagline__lead { font-weight: 900; font-size: 14px; letter-spacing: 0.4px; }
  .tagline__list { font-size: 14px; margin-top: 2px; }
</style>
</head>
<body>

  <section class="card card--front" aria-label="Business card front">
    <div class="brand">
      <span class="brand__mark"></span>
      <span class="brand__name">Brolga Ridge Excavations Pty Ltd</span>
    </div>

    <div class="divider"></div>

    <div class="details">
      <p class="details__name">Harold Benton</p>
      <p class="details__role">Managing Director</p>
      <p class="details__company">Brolga Ridge Excavations Pty Ltd</p>
      <p class="details__address">82 Gumleaf Creek Road<br>Moree NSW 2400</p>
      <ul class="contact">
        <li>
          <svg viewBox="0 0 12 12" aria-hidden="true"><path fill="#f5891f" d="M2.5 1h2l1 2.6-1.3 1a6.5 6.5 0 0 0 3.2 3.2l1-1.3L11 7.5v2a1.3 1.3 0 0 1-1.4 1.3A9.5 9.5 0 0 1 1.2 2.4 1.3 1.3 0 0 1 2.5 1z"/></svg>
          0418 639 204
        </li>
        <li>
          <svg viewBox="0 0 12 12" aria-hidden="true"><rect x="0.5" y="2" width="11" height="8" rx="1" fill="#f5891f"/><path d="M1 2.6 6 6.4l5-3.8" fill="none" stroke="#fcf8f7" stroke-width="1"/></svg>
          haroldbenton@brolgaridgeexc.com.au
        </li>
        <li>
          <svg viewBox="0 0 12 12" aria-hidden="true"><circle cx="6" cy="6" r="5.5" fill="#f5891f"/><path d="M0.8 6h10.4M6 0.6c-2 2.8-2 8 0 10.8M6 0.6c2 2.8 2 8 0 10.8" fill="none" stroke="#fcf8f7" stroke-width="0.8"/></svg>
          www.brolgaridgeexc.com.au
        </li>
      </ul>
    </div>

    <svg class="abn-band" width="540" height="330" viewBox="0 0 540 330" aria-hidden="true">
      <polygon points="0,228 290,228 270,264 0,264" fill="#3b3b3b"/>
      <polygon points="266,270 540,270 540,330 232,330" fill="#f5891f"/>
    </svg>
    <p class="abn"><span class="abn__label">ABN</span> 58 402 937 615</p>
  </section>

  <section class="card card--back" aria-label="Business card back">
    <div class="back__brand">
      <span class="back__mark"></span>
      <span class="back__name">Brolga Ridge Excavations</span>
    </div>
    <div class="tagline">
      <p class="tagline__lead">WE SPECIALISE IN</p>
      <p class="tagline__list">Agriculture, Civil Construction and Mining.</p>
    </div>
  </section>

</body>
</html>
```